Business Cards and Stationery incorporating Logo design
Business Cards and Stationery incorporating Logo design -
Creative Brief
Professional
Daniel P. Halvorsen
Managing Director
418 Corvane Tower 9th Fl. Uniondale, NY 11553
1-555-hdg-cash
dhalvorsen@halvorsendrakeco.example
www.halvorsendrakeco.example

```html
<!DOCTYPE html>
<html lang="en">
<head>
<meta charset="utf-8">
<title>Halvorsen Drake – Business Card</title>
<link href="https://fonts.googleapis.com/css2?family=PT+Sans:ital,wght@0,400;1,400;1,700&family=Tinos:wght@400;700&display=swap" rel="stylesheet">
<style>
  :root {
    --backdrop: #3b3b3b;
    --brand-green: #1f6b3a;
    --brand-green-dark: #175a30;
    --card-white: #ffffff;
    --ink-light: #f4f7f4;
  }
  * { box-sizing: border-box; margin: 0; padding: 0; }
  html, body {
    width: 1200px;
    height: 780px;
    overflow: hidden;
    background: var(--backdrop);
  }
  .canvas {
    position: relative;
    width: 1200px;
    height: 780px;
  }
  .business-card {
    position: absolute;
    left: 80px;
    top: 93px;
    width: 1040px;
    height: 594px;
    border-radius: 30px;
    overflow: hidden;
    background: var(--card-white);
    display: flex;
    box-shadow: 0 10px 28px rgba(0,0,0,.35);
  }
  .contact-panel {
    position: relative;
    width: 478px;
    height: 100%;
    background: var(--brand-green);
    color: var(--ink-light);
    padding: 76px 0 0 28px;
  }
  .divider-rule {
    width: 5px;
    height: 100%;
    margin-left: 8px;
    background: var(--brand-green-dark);
  }
  .person-name {
    font-family: "PT Sans", sans-serif;
    font-style: italic;
    font-weight: 700;
    font-size: 26px;
    letter-spacing: .2px;
  }
  .person-title {
    font-family: "PT Sans", sans-serif;
    font-style: italic;
    font-weight: 700;
    font-size: 19px;
    margin-top: 4px;
  }
  .contact-details {
    position: absolute;
    left: 28px;
    top: 350px;
    font-family: "Tinos", serif;
    font-size: 20px;
    line-height: 1.3;
  }
  .address { margin-bottom: 14px; }
  .phone-line {
    display: flex;
    align-items: center;
    gap: 12px;
    line-height: 1.55;
  }
  .phone-line svg { width: 18px; height: 18px; flex: none; }
  .identity-panel {
    flex: 1;
    display: flex;
    flex-direction: column;
    align-items: center;
    justify-content: center;
    padding-top: 10px;
  }
  .brand-square {
    width: 74px;
    height: 74px;
    background: var(--brand-green);
    margin-bottom: 24px;
  }
  .brand-name {
    font-family: "Tinos", serif;
    font-weight: 700;
    color: var(--brand-green);
    font-size: 56px;
    line-height: 1.0;
    text-align: center;
    font-variant: small-caps;
    letter-spacing: 1px;
  }
</style>
</head>
<body>
<div class="canvas">
  <div class="business-card">
    <section class="contact-panel">
      <h1 class="person-name">Daniel P. Halvorsen</h1>
      <p class="person-title">Managing Director</p>

      <div class="contact-details">
        <p class="address">418 Corvane Tower<br>9th Fl. Brackenford, NJ 07553</p>
        <p class="phone-line">
          <svg viewBox="0 0 24 24" aria-hidden="true"><path fill="currentColor" d="M6.6 10.8a15.1 15.1 0 0 0 6.6 6.6l2.2-2.2a1 1 0 0 1 1-.25 11.4 11.4 0 0 0 3.6.57 1 1 0 0 1 1 1V20a1 1 0 0 1-1 1A17 17 0 0 1 3 4a1 1 0 0 1 1-1h3.5a1 1 0 0 1 1 1c0 1.25.2 2.46.57 3.6a1 1 0 0 1-.25 1z"/></svg>
          1-555-hdg-cash
        </p>
        <p class="phone-line">
          <svg viewBox="0 0 24 24" aria-hidden="true"><path fill="currentColor" d="M6.6 10.8a15.1 15.1 0 0 0 6.6 6.6l2.2-2.2a1 1 0 0 1 1-.25 11.4 11.4 0 0 0 3.6.57 1 1 0 0 1 1 1V20a1 1 0 0 1-1 1A17 17 0 0 1 3 4a1 1 0 0 1 1-1h3.5a1 1 0 0 1 1 1c0 1.25.2 2.46.57 3.6a1 1 0 0 1-.25 1z"/></svg>
          (555) 014-6230
        </p>
        <p class="phone-line">
          <svg viewBox="0 0 24 24" aria-hidden="true"><rect x="6" y="2" width="12" height="20" rx="2" fill="currentColor"/><rect x="8" y="5" width="8" height="11" fill="#1f6b3a"/><circle cx="12" cy="19" r="1.2" fill="#1f6b3a"/></svg>
          (555) 017-8842
        </p>
      </div>
    </section>
    <div class="divider-rule"></div>
    <section class="identity-panel">
      <div class="brand-square"></div>
      <p class="brand-name">Halvorsen<br>Drake</p>
    </section>
  </div>
</div>
</body>
</html>
```